The First Annual Tamsworth Legacy Supper

Something similar to the attached but an attention grabber. It needs to attract people with money to spend!

```html
<!DOCTYPE html>
<html lang="en">
<head>
<meta charset="utf-8">
<title>The First Annual Tamsworth Legacy Supper</title>
<link rel="stylesheet" href="https://fonts.googleapis.com/css2?family=Montserrat:wght@500;600;700;800;900&family=Outfit:wght@300;400;600;700&family=Playfair+Display:ital,wght@0,900;1,900&display=swap">
<style>
  :root {
    --navy: #283583;
    --red: #d0181c;
    --white: #ffffff;
    --ink: #1d1d22;
    --backdrop: #1078bb;
    --sky-top: #5d8fd0;
    --sky-low: #c9dcef;
    --grass: #7d8a4a;
  }
  * { margin: 0; padding: 0; box-sizing: border-box; }
  html, body {
    width: 1200px; height: 1200px; overflow: hidden;
    background: var(--backdrop);
  }
  .flyer {
    position: absolute; left: 152px; top: 20px;
    width: 896px; height: 1160px;
    background: var(--white);
    overflow: hidden;
    font-family: "Outfit", sans-serif;
    color: var(--ink);
  }
  .hero-photo {
    position: absolute; left: 53px; top: 0; width: 790px; height: 382px;
    background: linear-gradient(180deg, var(--sky-top) 0%, var(--sky-low) 45%, #e9eef3 62%, #b9b8a0 78%, var(--grass) 100%);
  }
  .masthead { position: absolute; left: 0; top: 0; width: 896px; height: 540px; }
  .masthead .presents { font-family: "Montserrat", sans-serif; font-weight: 700; font-size: 16px; fill: var(--white); }
  .masthead .badge-text { font-family: "Playfair Display", serif; font-weight: 900; fill: var(--white); }
  .masthead .title-block { font-family: "Montserrat", sans-serif; font-weight: 900; }
  .masthead .title-script { font-family: "Playfair Display", serif; font-style: italic; font-weight: 900; fill: var(--red); }

  .event-date {
    position: absolute; left: 205px; top: 532px; width: 487px;
    display: flex; justify-content: center; align-items: center;
    color: var(--navy); font-family: "Montserrat", sans-serif;
    padding-bottom: 8px; border-bottom: 2px solid var(--red);
  }
  .event-date .month, .event-date .year { font-weight: 500; font-size: 40px; letter-spacing: 8px; }
  .event-date .day {
    font-weight: 800; font-size: 72px; line-height: 1;
    padding: 0 18px; margin: 0 16px 0 8px;
    border-left: 2px solid var(--red); border-right: 2px solid var(--red);
  }
  .event-time {
    position: absolute; left: 205px; top: 616px; width: 487px;
    text-align: center; color: var(--navy); font-family: "Montserrat", sans-serif;
    border-bottom: 2px solid var(--red); padding-bottom: 4px;
  }
  .event-time .lead, .event-time .tail { font-weight: 500; font-size: 20px; letter-spacing: 6px; line-height: 1.1; }
  .event-time .hour { font-weight: 800; font-size: 58px; letter-spacing: 2px; line-height: 1; }

  .highlights {
    position: absolute; left: 53px; top: 734px; width: 790px; text-align: center;
    font-family: "Montserrat", sans-serif; font-weight: 800; font-size: 22px;
    letter-spacing: 0.6px; color: var(--navy); white-space: nowrap; line-height: 28px;
  }
  .story {
    position: absolute; left: 53px; top: 766px; width: 790px;
    display: grid; grid-template-columns: 387px 383px; column-gap: 20px;
    font-size: 15.4px; font-weight: 400; line-height: 20.5px;
  }
  .story p + p { margin-top: 20.5px; }
  .social-note {
    display: flex; align-items: center; gap: 12px; margin-top: 16px;
    color: var(--navy); font-weight: 700; font-size: 13.5px; line-height: 18px;
  }
  .social-note .dot { flex: 0 0 28px; height: 28px; border-radius: 50%; background: var(--navy); }

  .ticket-band {
    position: absolute; left: 0; top: 958px; width: 896px; height: 202px;
    background: var(--red); color: var(--white);
  }
  .ticket-band .prices {
    position: absolute; left: 53px; top: 24px; width: 285px;
    font-weight: 700; font-size: 15.5px; line-height: 22px; text-transform: uppercase;
  }
  .ticket-band .prices p + p { margin-top: 22px; }
  .ticket-band .outlets { position: absolute; left: 394px; top: 24px; width: 290px; font-size: 15.5px; line-height: 20.5px; }
  .ticket-band .contacts { position: absolute; left: 698px; top: 24px; width: 150px; font-size: 15.5px; line-height: 20.5px; }
  .ticket-band h3 {
    display: inline-block; font-size: 17px; font-weight: 700;
    border-bottom: 2px solid var(--white); padding-bottom: 1px; margin-bottom: 8px;
  }
  .ticket-band strong { font-weight: 700; display: block; }
  .ticket-band span { font-weight: 300; display: block; }
</style>
</head>
<body>
<main class="flyer">
  <div class="hero-photo" role="img" aria-label="Photo of a long white clapboard community hall with a pale metal roof under a blue cloudy sky, on a grassy lot"></div>

  <svg class="masthead" viewBox="0 0 896 540" xmlns="http://www.w3.org/2000/svg">
    <rect x="190" y="273" width="518" height="27" fill="#283583"/>
    <text class="presents" x="202" y="292.5" textLength="494" lengthAdjust="spacingAndGlyphs">THE TAMSWORTH COMMUNITY CENTER PRESENTS</text>

    <circle cx="178" cy="383" r="71" fill="#d0181c"/>
    <text class="badge-text" x="178" y="348" text-anchor="middle" font-size="20">The</text>
    <text class="badge-text" x="176" y="414" text-anchor="middle" font-size="74" letter-spacing="-3">1st</text>
    <text class="badge-text" x="178" y="443" text-anchor="middle" font-size="19">Annual</text>

    <text class="title-block" x="266" y="381" font-size="92" fill="#ffffff" textLength="570" lengthAdjust="spacingAndGlyphs">TAMSWORTH</text>
    <text class="title-block" x="268" y="455" font-size="96" fill="#283583" letter-spacing="-1">LEGACY</text>
    <text class="title-script" x="290" y="500" font-size="76">Supper</text>
  </svg>

  <div class="event-date">
    <span class="month">APRIL</span>
    <span class="day">23</span>
    <span class="year">2022</span>
  </div>

  <div class="event-time">
    <div class="lead">STARTING AT</div>
    <div class="hour">5:00PM</div>
    <div class="tail">WITH COCKTAIL HOUR</div>
  </div>

  <h2 class="highlights">LIVE AUCTION, SILENT AUCTION, RAFFLE AND A CASH BAR!</h2>

  <section class="story">
    <div class="story-col">
      <p>Come on out to the Tamsworth Community Center for a delicious prime rib dinner, drinks, entertainment and more! There will be plenty of amazing auction items for everyone to choose from.</p>
      <p>All proceeds will go to the Tamsworth Community Center. We will share some history of the school and each year we will highlight a local family. This year</p>
    </div>
    <div class="story-col">
      <p>will be the Harlow family who have been here for .... years!!</p>
      <p>High Side Barn, dirt bike, custom knives, a pack trip and so much more!</p>
      <div class="social-note">
        <span class="dot"></span>
        <span>Follow the Tamsworth Community Center's Townboard page to see all the auction items available!</span>
      </div>
    </div>
  </section>

  <footer class="ticket-band">
    <div class="prices">
      <p>Tickets for the event are $50 each or $90 for a couple</p>
      <p>Tickets for the 10x12 high side barn $25 each or 5 for $100. Donated by: Ridgeline Shed Co. of Carver Falls, value $6500</p>
    </div>
    <div class="outlets">
      <h3>Get your tickets from:</h3>
      <strong>Ridgeline Shed Co. in Carver Falls</strong>
      <span>412 Alder Bend Rd, Carver Falls</span>
      <strong>Summit Trail Realty</strong>
      <span>26 W Cedar Ave, Carver Falls</span>
      <strong>Tamsworth Mercantile</strong>
      <span>5120 County Road 88, Tamsworth</span>
    </div>
    <div class="contacts">
      <h3>Or get them from</h3>
      <strong>Marla Quint -</strong>
      <span>(555)210-4418</span>
      <strong>Dana Forsell -</strong>
      <span>(555)382-9076</span>
    </div>
  </footer>
</main>
</body>
</html>
```